Brochure Design Project

asphalt paving contractor needs folder brochure design. this folder will be able to hold flyers, business card, proposals, etc. the design is mostly for front and back of folder. our main focus is being a service provider in the relationship building business, brochure/folder should come across as such. professional, inviting, warm, eye catching, and trendi.attached is our business card design and logo we don't want to change this only for refrence and brochure/folder needs to be different.
Updates

please review new updates

remember we are dealing with top executives, they know what asphalt looks like they dont need a sample of it. again focus needs to be moreĀ on customer relationships. shaking hands, building blocks, missing puzzle, thinking outside the box, these are all good examples i'm open to.

also much lighter colors many customers are females and again they know what asphalt looks like and i dont want my logo overpowering on this cover. this is not about us its about them.

Target Market(s)

CEO'S, Executives, Upper Management

Industry/Entity Type

Contractor

Requirements
Must have
• an inviting, warm yet still professional cover with more focus on the relationships build and retain.
Should not have
• our logo and color scheme should not be higly advocated on folder cover.

```html
<!DOCTYPE html>
<html lang="en">
<head>
<meta charset="utf-8">
<title>Harbor Paving – Presentation Folder</title>
<link rel="stylesheet" href="https://fonts.googleapis.com/css2?family=Marcellus&family=Open+Sans:wght@400&display=swap">
<style>
  :root {
    --canvas: #ffffff;
    --panel: #fbfbfa;
    --panel-edge: #ecebe6;
    --olive: #7a6a22;
    --olive-dark: #5e5116;
    --gold: #b39a3a;
    --sand: #ddd2b4;
    --tile-yellow: #f7cf4a;
    --tile-orange: #ef8a2e;
    --tile-peach: #f8c79a;
    --text-brand: #7a6a22;
  }
  * { margin: 0; padding: 0; box-sizing: border-box; }
  html, body {
    width: 1200px; height: 800px; overflow: hidden;
    background: var(--canvas);
  }
  .canvas { position: relative; width: 1200px; height: 800px; }
  .folder-panel {
    position: absolute; top: 60px;
    width: 482px; height: 673px;
    background: var(--panel);
    border: 1px solid var(--panel-edge);
    overflow: hidden;
  }
  .folder-panel--front { left: 69px; }
  .folder-panel--back { left: 637px; background: #ffffff; }
  .folder-art { position: absolute; inset: 0; width: 100%; height: 100%; }
  .brand {
    position: absolute; left: 0; right: 0;
    display: flex; justify-content: center;
    color: var(--text-brand);
  }
  .brand__lockup { display: inline-flex; flex-direction: column; align-items: flex-end; }
  .folder-panel--front .brand { top: 530px; }
  .folder-panel--back .brand { top: 292px; }
  .brand__name {
    font-family: "Marcellus", serif;
    font-size: 26px; letter-spacing: 1px; line-height: 1;
    white-space: nowrap;
  }
  .brand__tagline {
    font-family: "Open Sans", sans-serif;
    font-size: 10px; line-height: 1.2; margin-top: 3px;
    white-space: nowrap;
  }
</style>
</head>
<body>
<main class="canvas">

  <section class="folder-panel folder-panel--front">
    <svg class="folder-art" viewBox="0 0 482 673">
      <defs>
        <linearGradient id="tileWarm" x1="0" y1="0" x2="1" y2="1">
          <stop offset="0" stop-color="var(--tile-yellow)"/>
          <stop offset="0.45" stop-color="var(--tile-orange)"/>
          <stop offset="0.75" stop-color="var(--tile-peach)"/>
          <stop offset="1" stop-color="var(--tile-orange)"/>
        </linearGradient>
        <linearGradient id="oliveBand" x1="0" y1="0" x2="1" y2="0">
          <stop offset="0" stop-color="var(--olive-dark)"/>
          <stop offset="0.6" stop-color="var(--olive)"/>
          <stop offset="1" stop-color="var(--gold)"/>
        </linearGradient>
      </defs>
      <path role="img" aria-label="Warm mosaic of small yellow and orange tiles sweeping in a wave"
            fill="url(#tileWarm)"
            d="M0 0 H482 V110 C440 130 405 195 365 280 C325 360 250 390 160 362 C100 342 40 312 0 310 Z"/>
      <path fill="none" stroke="var(--sand)" stroke-width="5"
            d="M0 352 C60 356 110 378 170 398 C260 422 340 385 380 300 C415 225 445 170 482 158"/>
      <path fill="none" stroke="url(#oliveBand)" stroke-width="20"
            d="M0 322 C40 324 100 348 160 372 C250 404 330 372 370 292 C410 202 440 142 482 127"/>
    </svg>
    <div class="brand">
      <div class="brand__lockup">
        <p class="brand__name">HARBOR PAVING</p>
        <p class="brand__tagline">Partners Before Pavement</p>
      </div>
    </div>
  </section>

  <section class="folder-panel folder-panel--back">
    <svg class="folder-art" viewBox="0 0 482 673">
      <defs>
        <linearGradient id="tileWarmBack" x1="0" y1="1" x2="1" y2="0">
          <stop offset="0" stop-color="var(--tile-yellow)"/>
          <stop offset="0.5" stop-color="var(--tile-peach)"/>
          <stop offset="1" stop-color="var(--tile-orange)"/>
        </linearGradient>
        <linearGradient id="oliveBandBack" x1="0" y1="0" x2="1" y2="0">
          <stop offset="0" stop-color="var(--gold)"/>
          <stop offset="0.5" stop-color="var(--olive)"/>
          <stop offset="1" stop-color="var(--olive-dark)"/>
        </linearGradient>
      </defs>
      <path fill="none" stroke="var(--sand)" stroke-width="5"
            d="M110 673 C170 595 245 520 330 512 C400 506 450 528 482 545"/>
      <path role="img" aria-label="Warm mosaic of small yellow and orange tiles rising in a wave"
            fill="url(#tileWarmBack)"
            d="M140 673 C195 610 262 545 335 538 C400 532 450 552 482 570 V673 Z"/>
      <path fill="none" stroke="url(#oliveBandBack)" stroke-width="18"
            d="M132 673 C187 607 257 539 332 531 C400 524 450 545 482 562"/>
    </svg>
    <div class="brand">
      <div class="brand__lockup">
        <p class="brand__name">HARBOR PAVING</p>
        <p class="brand__tagline">Partners Before Pavement</p>
      </div>
    </div>
  </section>

</main>
</body>
</html>
```